Storm Restoration Contractor needs a professional business card design

Looking for a professional business card design. Not looking for your cheapo MS Word standard ones that are readily available. Dont want it to be cookie cutter look like ones readily available online. We just recently changed our logo and want to freshen up all our documents. Our company handles restoring a property back to a pre-loss condition after a storm damages it. For example, wind, hail, flood, fire losses.

Target Market(s)

Property Owners, Homeowners, Property Owners, Commercial Property Owners, Property Management Companies, Hail and Wind Damaged Properties

Industry/Entity Type

Construction Company

Contact Information for Business Card

Brightline Facades
847-555-0193
847-555-0147 fax
www.brightlinefacades.example
info@brightlinefacades.example

Requirements
Must have
• Clean, Professional, fresh look
• Storm Restoration, Roofing, Siding, Windows
Nice to have
• If there is a way to incorporate storms that may be cool.

```html
<!DOCTYPE html>
<html lang="en">
<head>
<meta charset="utf-8">
<title>Brightline Facades – Business Card</title>
<link href="https://fonts.googleapis.com/css2?family=Oswald:wght@500;600&family=Open+Sans:wght@400;600&display=swap" rel="stylesheet">
<style>
  :root {
    --bg: #2b2b2d;
    --card: #ffffff;
    --ink: #3a3a3c;
    --blue: #1f78c8;
    --dark: #333335;
    --light-text: #f2f2f2;
  }
  html, body {
    margin: 0;
    width: 1200px;
    height: 1000px;
    overflow: hidden;
    background: var(--bg);
  }
  .canvas {
    position: relative;
    width: 1200px;
    height: 1000px;
  }
  .card {
    position: absolute;
    left: 232px;
    width: 735px;
    height: 420px;
    border-radius: 34px;
    background: var(--card);
    overflow: hidden;
    box-shadow: 0 14px 30px rgba(0,0,0,0.35);
  }
  .card-front { top: 60px; }
  .card-back { top: 520px; }

  .brand {
    display: flex;
    align-items: center;
    gap: 18px;
  }
  .brand-dot {
    width: 74px;
    height: 74px;
    border-radius: 50%;
    background: var(--blue);
    flex: none;
  }
  .brand-name {
    font-family: "Oswald", sans-serif;
    font-weight: 600;
    color: var(--blue);
    text-transform: uppercase;
    line-height: 0.95;
    letter-spacing: 1px;
  }
  .card-front .brand {
    position: absolute;
    left: 50%;
    top: 50%;
    transform: translate(-50%, -50%);
  }
  .card-front .brand-name { font-size: 46px; }

  .card-back .brand {
    position: absolute;
    right: 44px;
    top: 46px;
    gap: 12px;
  }
  .card-back .brand-dot { width: 48px; height: 48px; }
  .card-back .brand-name { font-size: 30px; }

  .back-shape {
    position: absolute;
    inset: 0;
  }
  .holder {
    position: absolute;
    left: 58px;
    top: 150px;
  }
  .holder-company {
    font-family: "Oswald", sans-serif;
    font-weight: 600;
    font-size: 27px;
    color: var(--ink);
    text-transform: uppercase;
    letter-spacing: 0.5px;
    margin: 0;
  }
  .holder-company .accent { color: var(--blue); }
  .holder-role {
    font-family: "Open Sans", sans-serif;
    font-size: 16px;
    color: var(--ink);
    margin: 2px 0 0;
  }

  .contact-list {
    position: absolute;
    left: 112px;
    top: 286px;
    margin: 0;
    padding: 0;
    list-style: none;
    font-family: "Open Sans", sans-serif;
    font-size: 17px;
    color: var(--light-text);
  }
  .contact-list li {
    display: flex;
    align-items: center;
    gap: 12px;
    height: 28px;
  }
  .contact-list svg { width: 14px; height: 14px; fill: var(--blue); flex: none; }
  .contact-list .web-accent { color: var(--blue); }

  .address {
    position: absolute;
    right: 44px;
    top: 185px;
    text-align: right;
    font-family: "Open Sans", sans-serif;
    font-size: 17px;
    line-height: 1.35;
    color: var(--light-text);
  }
  .address svg { width: 14px; height: 18px; fill: var(--blue); display: block; margin: 0 0 6px auto; }
</style>
</head>
<body>
<main class="canvas">

  <section class="card card-front" aria-label="Card front">
    <div class="brand">
      <span class="brand-dot"></span>
      <span class="brand-name">Brightline<br>Facades</span>
    </div>
  </section>

  <section class="card card-back" aria-label="Card back">
    <svg class="back-shape" viewBox="0 0 735 420" preserveAspectRatio="none">
      <path d="M0,386 C80,226 300,156 735,131 L735,420 L0,420 Z" fill="var(--blue)"/>
      <path d="M0,400 C80,240 300,170 735,145 L735,420 L0,420 Z" fill="var(--dark)"/>
    </svg>

    <div class="brand">
      <span class="brand-dot"></span>
      <span class="brand-name">Brightline<br>Facades</span>
    </div>

    <div class="holder">
      <p class="holder-company">Brightline <span class="accent">Facades</span></p>
      <p class="holder-role">CEO</p>
    </div>

    <ul class="contact-list">
      <li>
        <svg viewBox="0 0 24 24"><path d="M6.6 10.8a15.1 15.1 0 0 0 6.6 6.6l2.2-2.2c.3-.3.7-.4 1-.2 1.1.4 2.3.6 3.6.6.6 0 1 .4 1 1V20c0 .6-.4 1-1 1A17 17 0 0 1 3 4c0-.6.4-1 1-1h3.5c.6 0 1 .4 1 1 0 1.3.2 2.5.6 3.6.1.3 0 .7-.2 1z"/></svg>
        <span>847-555-0193</span>
      </li>
      <li>
        <svg viewBox="0 0 24 24"><path d="M6 3h10v5H6zM3 9h18v9h-3v3H6v-3H3zm5 6v4h8v-4z"/></svg>
        <span>847-555-0147</span>
      </li>
      <li>
        <svg viewBox="0 0 24 24"><path d="M2 5h20v14H2zm2 2v.5l8 5 8-5V7z"/></svg>
        <span>info@brightlinefacades.example</span>
      </li>
      <li>
        <svg viewBox="0 0 24 24"><path d="M12 2a10 10 0 1 0 0 20 10 10 0 0 0 0-20zm6.9 9h-3a15 15 0 0 0-1.3-5.6A8 8 0 0 1 18.9 11zM12 4c.9 1.3 1.7 3.9 1.9 7h-3.8c.2-3.1 1-5.7 1.9-7zM4.1 13h3a15 15 0 0 0 1.3 5.6A8 8 0 0 1 4.1 13zm3-2h-3a8 8 0 0 1 4.3-5.6A15 15 0 0 0 7.1 11zm3 2h3.8c-.2 3.1-1 5.7-1.9 7-.9-1.3-1.7-3.9-1.9-7zm5.5 5.6a15 15 0 0 0 1.3-5.6h3a8 8 0 0 1-4.3 5.6z"/></svg>
        <span>www.<span class="web-accent">brightlinefacades</span>.example</span>
      </li>
    </ul>

    <address class="address">
      <svg viewBox="0 0 24 30"><path d="M12 0a10 10 0 0 0-10 10c0 7.5 10 20 10 20s10-12.5 10-20A10 10 0 0 0 12 0zm0 14a4 4 0 1 1 0-8 4 4 0 0 1 0 8z"/></svg>
      Your Street Address,<br>Singapore, 1234
    </address>
  </section>

</main>
</body>
</html>
```